Quorvel Marketing & Design needs a Wordpress website

We need a wordpress design for a new marketing and design company in Australia called 'Quorvel Marketing & Design". The website needs to be responsive, modern, and attract new customers. It needs to be unique and different. We provide marketing and design solutions for small businesses from consulting, to flyer distribution to Facebook ads etc. We would like to see designs that use the Quorvel logo colours. The final design should communicate professionalism, creativity & growth. It needs to stand out from the crowd.

Target Market(s)

Small Business who need a marketing freelancer to help them grow

Industry/Entity Type

Marketing

Number of Pages Required

3 page

Requirements
Must have
• Home page, services page & contact page

```html
<!DOCTYPE html>
<html lang="en">
<head>
<meta charset="utf-8">
<title>Quorvel Marketing &amp; Design</title>
<link href="https://fonts.googleapis.com/css2?family=Roboto:wght@300;400;500;700&family=Open+Sans:wght@400;600&display=swap" rel="stylesheet">
<style>
:root{
  --pink:#e6138c;
  --pink-dark:#c70c77;
  --pink-soft:#f04aa6;
  --ink:#222;
  --muted:#666;
  --line:#ddd;
  --white:#fff;
  --navy:#3a3f6e;
}
*{box-sizing:border-box;margin:0;padding:0}
html,body{width:723px;height:1200px;overflow:hidden;background:#fff}
body{font-family:"Open Sans",Arial,sans-serif;color:var(--ink);position:relative}
.topbar{position:absolute;left:0;top:0;width:723px;height:38px;background:var(--pink)}
.socials{position:absolute;right:24px;top:10px;display:flex;gap:20px}
.socials span{width:16px;height:16px;border-radius:50%;background:var(--white);opacity:.9}
.brand{position:absolute;left:24px;top:0;width:242px;height:84px;background:#fff;box-shadow:0 2px 6px rgba(0,0,0,.25);z-index:3;display:flex;align-items:center;gap:12px;padding-left:22px}
.brand-dot{width:38px;height:38px;border-radius:50%;background:var(--pink)}
.brand-name{font-family:"Roboto",sans-serif;font-weight:700;font-size:24px;color:var(--navy);line-height:1.05}
.brand-name small{display:block;font-size:11px;letter-spacing:1px}
.nav{position:absolute;left:0;top:38px;width:723px;height:20px;background:var(--pink-dark);z-index:2}
.nav ul{list-style:none;display:flex;position:absolute;left:280px;top:0}
.nav li{font-family:"Roboto",sans-serif;font-size:10px;color:#fff;text-transform:uppercase;padding:4px 18px 0;height:20px}
.nav li.active{background:var(--pink)}
.hero{position:absolute;left:0;top:58px;width:723px;height:280px;background:linear-gradient(180deg,#dfe6ee 0%,#b9c6d3 55%,#8a98a8 100%)}
.hero-people{position:absolute;right:80px;top:0;width:330px;height:280px;background:linear-gradient(180deg,#6a7080,#2d3340);opacity:.55}
.hero-copy{position:absolute;left:29px;top:36px;width:290px}
.hero-copy h1{font-family:"Roboto",sans-serif;font-weight:400;font-size:29px;line-height:1.08;color:var(--ink)}
.hero-copy p{margin-top:8px;background:var(--pink);color:#fff;font-size:11px;line-height:1.35;padding:3px 6px;width:270px}
.arrow{position:absolute;top:114px;width:22px;height:32px;background:rgba(40,40,40,.7)}
.arrow.l{left:6px}.arrow.r{right:6px}
.services{position:absolute;left:0;top:338px;width:723px;height:160px;background:linear-gradient(180deg,#f3f3f3,#fff)}
.service{position:absolute;top:18px;width:160px;text-align:center}
.service .ic{width:84px;height:84px;margin:0 auto;border-radius:50%;background:var(--pink);border:5px solid #e9e9e9;box-shadow:0 3px 6px rgba(0,0,0,.2)}
.service h3{font-family:"Roboto",sans-serif;font-weight:400;font-size:17px;margin-top:12px;line-height:1.15}
.divider{position:absolute;left:48px;top:508px;width:627px;height:1px;background:var(--line)}
.about h2{position:absolute;left:0;width:723px;top:524px;text-align:center;font-family:"Roboto",sans-serif;font-weight:300;font-size:34px;line-height:40px;color:var(--pink)}
.about p{position:absolute;left:48px;top:604px;width:380px;font-size:11px;line-height:1.75;color:var(--muted)}
.btn{position:absolute;left:48px;top:706px;width:104px;height:34px;background:var(--pink);color:#fff;font-size:13px;text-align:center;line-height:34px}
.about-photo{position:absolute;left:494px;top:574px;width:190px;height:209px;background:linear-gradient(160deg,#dde3ea,#2f3545)}
.cols{position:absolute;left:0;top:807px;width:723px;height:230px}
.col{position:absolute;top:0;width:190px;height:210px}
.col h4{font-family:"Roboto",sans-serif;font-weight:500;font-size:14px;color:var(--pink);margin-bottom:20px}
.post{margin-bottom:18px;font-size:8px;line-height:1.45;color:var(--muted)}
.post b{display:block;color:var(--ink);font-size:9px}
.post em{font-style:normal;color:var(--pink)}
.vline{position:absolute;top:0;width:2px;height:230px;background:var(--navy)}
.viewall{position:absolute;bottom:0;font-size:10px;color:var(--pink);text-decoration:underline}
.avatar{width:40px;height:40px;border-radius:50%;background:var(--pink-soft);margin:0 auto 12px}
.testi{text-align:center;font-size:8px;line-height:1.45;color:var(--muted)}
.footer{position:absolute;left:0;top:1053px;width:723px;height:147px;background:var(--pink)}
.fnav{position:absolute;left:48px;top:22px;display:flex;gap:26px;font-size:11px;color:#fff}
.fsoc{position:absolute;right:48px;top:22px;display:flex;gap:20px}
.fsoc span{width:13px;height:13px;border-radius:50%;background:#fff}
.contact{position:absolute;top:70px;display:flex;align-items:center;gap:8px;color:#fff;font-size:10px;line-height:1.3}
.contact svg{flex:none}
.copy{position:absolute;left:0;bottom:0;width:723px;height:30px;background:var(--pink-dark);color:#fff;font-size:9px;text-align:center;line-height:30px}
</style>
</head>
<body>
<header>
  <div class="topbar">
    <div class="socials" aria-label="Social links"><span></span><span></span><span></span></div>
  </div>
  <div class="brand"><span class="brand-dot"></span><div class="brand-name">Quorvel<small>MARKETING &amp; DESIGN</small></div></div>
  <nav class="nav"><ul><li class="active">Home</li><li>About Us</li><li>Services</li><li>Clients</li><li>Contact Us</li></ul></nav>
</header>

<section class="hero">
  <div class="hero-people" role="img" aria-label="Two business people standing in front of a city skyline"></div>
  <div class="hero-copy">
    <h1>Looking for some marketing expertise</h1>
    <p>You've come to the right place. It might just be that you want some solid marketing advice.</p>
  </div>
  <svg class="arrow l" viewBox="0 0 22 32"><path d="M14 10 L8 16 L14 22" stroke="#fff" stroke-width="2" fill="none"/></svg>
  <svg class="arrow r" viewBox="0 0 22 32"><path d="M8 10 L14 16 L8 22" stroke="#fff" stroke-width="2" fill="none"/></svg>
</section>

<section class="services">
  <div class="service" style="left:53px"><div class="ic"><svg width="74" height="74" viewBox="0 0 74 74"><path d="M30 48 L44 26 L48 29 L34 50 Z" fill="#fff"/><path d="M30 48 L29 53 L34 50Z" fill="#fff"/></svg></div><h3>Logo Design</h3></div>
  <div class="service" style="left:204px"><div class="ic"><svg width="74" height="74" viewBox="0 0 74 74"><rect x="25" y="24" width="18" height="24" fill="#fff"/><rect x="34" y="32" width="16" height="20" fill="#fff" stroke="#e6138c" stroke-width="2"/></svg></div><h3>Corporate<br>Identity</h3></div>
  <div class="service" style="left:359px"><div class="ic"><svg width="74" height="74" viewBox="0 0 74 74"><rect x="26" y="22" width="22" height="28" fill="#fff"/><rect x="30" y="28" width="14" height="2" fill="#e6138c"/><rect x="30" y="33" width="14" height="2" fill="#e6138c"/><rect x="30" y="38" width="10" height="2" fill="#e6138c"/></svg></div><h3>Flyers</h3></div>
  <div class="service" style="left:506px"><div class="ic"><svg width="74" height="74" viewBox="0 0 74 74"><circle cx="37" cy="26" r="5" fill="#fff"/><circle cx="26" cy="36" r="4" fill="#fff"/><circle cx="48" cy="36" r="4" fill="#fff"/><path d="M30 50 a7 7 0 0 1 14 0Z M19 50 a7 7 0 0 1 14 0Z M41 50 a7 7 0 0 1 14 0Z" fill="#fff"/></svg></div><h3>Marketing<br>Consulting</h3></div>
</section>
<div class="divider"></div>

<section class="about">
  <h2>Know About Quorvel</h2>
  <p>Looking for some marketing expertise or have you started your own business and ready to take the plunge in getting your name out there. You've come to the right place. It might just be that you want some solid marketing advice and then do it yourself so you might want us to help you out. Whatever you decide is fine by us, and we're always here to help.</p>
  <div class="btn">Read More</div>
  <div class="about-photo" role="img" aria-label="Businessman holding a laptop with colourful marketing shapes rising from it"></div>
</section>

<section class="cols">
  <div class="col" style="left:60px">
    <h4>Latest News</h4>
    <div class="post">13 Jan 2015<b>Lorem Ipsum is simply dummy text.</b>Lorem Ipsum has been the industry's standard dummy text ever since the 1500s<br><em>Read More</em></div>
    <div class="post">20 Jan 2015<b>Lorem Ipsum is simply dummy text.</b>Lorem Ipsum has been the industry's standard dummy text ever since the 1500s<br><em>Read More</em></div>
    <span class="viewall" style="right:10px">View All</span>
  </div>
  <div class="vline" style="left:253px"></div>
  <div class="col" style="left:277px">
    <h4>Our Blog</h4>
    <div class="post">13 Jan 2015<b>Lorem Ipsum is simply dummy text.</b>Lorem Ipsum has been the industry's standard dummy text ever since the 1500s<br><em>Read More</em></div>
    <div class="post">20 Jan 2015<b>Lorem Ipsum is simply dummy text.</b>Lorem Ipsum has been the industry's standard dummy text ever since the 1500s<br><em>Read More</em></div>
    <span class="viewall" style="right:10px">View All</span>
  </div>
  <div class="vline" style="left:470px"></div>
  <div class="col" style="left:500px">
    <h4>Client Testimonial</h4>
    <div class="avatar" role="img" aria-label="Client portrait"></div>
    <div class="testi">Lorem Ipsum has been the industry's standard dummy text ever since the 1500s<br><br>Mara Linwood</div>
    <span class="viewall" style="right:0">View All</span>
  </div>
</section>

<footer class="footer">
  <div class="fnav"><span>Home</span><span>About</span><span>Services</span><span>Client</span><span>Contact</span></div>
  <div class="fsoc" aria-label="Social links"><span></span><span></span><span></span></div>
  <div class="contact" style="left:48px"><svg width="26" height="26" viewBox="0 0 26 26"><circle cx="13" cy="13" r="13" fill="#3a3f6e"/><path d="M13 6a5 5 0 0 0-5 5c0 4 5 9 5 9s5-5 5-9a5 5 0 0 0-5-5zm0 7a2 2 0 1 1 0-4 2 2 0 0 1 0 4z" fill="#fff"/></svg><span>Lorem Ipsum is simply<br>dummy text of the printing</span></div>
  <div class="contact" style="left:222px"><svg width="26" height="26" viewBox="0 0 26 26"><circle cx="13" cy="13" r="13" fill="#3a3f6e"/><path d="M9 7l3 0 1 4-2 1a8 8 0 0 0 4 4l1-2 4 1v3a2 2 0 0 1-2 1C12 19 7 14 7 9a2 2 0 0 1 2-2z" fill="#fff"/></svg><span>(02) 5550 1847</span></div>
  <div class="contact" style="left:380px"><svg width="26" height="26" viewBox="0 0 26 26"><circle cx="13" cy="13" r="13" fill="#3a3f6e"/><rect x="8" y="7" width="10" height="12" fill="#fff"/></svg><span>(02) 5550 1848</span></div>
  <div class="contact" style="left:532px"><svg width="26" height="26" viewBox="0 0 26 26"><circle cx="13" cy="13" r="13" fill="#3a3f6e"/><rect x="7" y="9" width="12" height="9" fill="#fff"/><path d="M7 9l6 5 6-5" stroke="#3a3f6e" fill="none"/></svg><span>hello@quorvel.com</span></div>
  <div class="copy">© Quorvel Design &amp; Marketing - 2015, All Rights Reserved &nbsp;|&nbsp; Terms &amp; Condition</div>
</footer>
</body>
</html>
```